Business Card Design

We need a business card designed for our new company. Prefer a black card with white logo & writing.

Contact Information for Business Card

Dov Telling, address: 3-4817 Fernwick Avenue, Abbotsford, BC, V8K 2P9, Office Phone: 604-913-2760, Cell: 604-271-4053, Email: dov@qlresinhaus.ca

Colors

Designer to choose only greyscale colors for use in the design.

```html
<!DOCTYPE html>
<html lang="en">
<head>
<meta charset="utf-8">
<title>QL Resin Haus – Business Card</title>
<link rel="stylesheet" href="https://fonts.googleapis.com/css2?family=Barlow+Condensed:wght@600;700&family=Barlow:wght@400;500&family=Sacramento&display=swap">
<style>
  :root {
    --backdrop: #e9e9e7;
    --card: #1a1a1a;
    --card-edge: #111111;
    --ink: #ffffff;
    --ink-soft: #bdbdbd;
    --texture-top: rgba(60, 60, 60, 0);
    --texture-mid: rgba(70, 70, 70, 0.55);
    --texture-low: rgba(40, 40, 40, 0.35);
  }
  * { box-sizing: border-box; margin: 0; padding: 0; }
  html, body {
    width: 1200px; height: 902px; overflow: hidden;
    background: var(--backdrop);
  }
  .canvas {
    width: 1200px; height: 902px;
    display: flex; align-items: center; justify-content: center; gap: 60px;
  }
  .card {
    position: relative;
    width: 520px; height: 297px;
    background: var(--card);
    border: 1px solid var(--card-edge);
    overflow: hidden;
    color: var(--ink);
  }
  .card__texture {
    position: absolute; left: 0; right: 0; bottom: 0; height: 140px;
    background: linear-gradient(180deg, var(--texture-top) 0%, var(--texture-mid) 55%, var(--texture-low) 100%);
  }
  /* Front */
  .front__name {
    position: absolute; left: 48px; top: 36px;
    font-family: "Barlow Condensed", sans-serif; font-weight: 700;
    font-size: 50px; letter-spacing: 1px; line-height: 1;
    text-transform: uppercase;
  }
  .front__surname {
    position: absolute; left: 58px; top: 84px;
    font-family: "Sacramento", cursive;
    font-size: 38px; color: var(--ink); line-height: 1;
  }
  .front__title {
    position: absolute; left: 48px; top: 182px;
    font-family: "Barlow", sans-serif; font-weight: 500;
    font-size: 12px; letter-spacing: 1px; color: var(--ink-soft);
    text-transform: uppercase;
  }
  .contact {
    position: absolute; left: 290px; top: 164px;
    list-style: none;
    font-family: "Barlow", sans-serif; font-size: 11px; line-height: 1.4;
    color: var(--ink);
  }
  .contact__item { display: flex; gap: 9px; margin-bottom: 7px; }
  .contact__icon { width: 12px; height: 12px; flex: none; margin-top: 1px; fill: var(--ink); }
  /* Back */
  .back__logo {
    position: absolute; left: 0; right: 0; top: 122px;
    text-align: center;
    font-family: "Barlow Condensed", sans-serif; font-weight: 700;
    font-size: 36px; letter-spacing: 1px; text-transform: uppercase;
  }
</style>
</head>
<body>
<main class="canvas">
  <section class="card card--front">
    <div class="card__texture" role="img" aria-label="Fine grey wavy line pattern across the lower card"></div>
    <h1 class="front__name">Dov Telling</h1>
    <p class="front__surname">Castellan</p>
    <p class="front__title">Founder &amp; CEO</p>
    <ul class="contact">
      <li class="contact__item">
        <svg class="contact__icon" viewBox="0 0 24 24"><path d="M6.6 10.8a15 15 0 0 0 6.6 6.6l2.2-2.2c.3-.3.7-.4 1-.2 1.1.4 2.3.6 3.6.6.6 0 1 .4 1 1V20c0 .6-.4 1-1 1A17 17 0 0 1 3 4c0-.6.4-1 1-1h3.5c.6 0 1 .4 1 1 0 1.3.2 2.5.6 3.6.1.3 0 .7-.2 1z"/></svg>
        <span>Office Phone: 604-913-2760<br>Cell: 604-271-4053</span>
      </li>
      <li class="contact__item">
        <svg class="contact__icon" viewBox="0 0 24 24"><path d="M2 5h20v14H2z M2 5l10 8 10-8" fill="none" stroke="#fff" stroke-width="2"/></svg>
        <span>dov@qlresinhaus.ca</span>
      </li>
      <li class="contact__item">
        <svg class="contact__icon" viewBox="0 0 24 24"><path d="M12 2a7 7 0 0 0-7 7c0 5 7 13 7 13s7-8 7-13a7 7 0 0 0-7-7zm0 9.5A2.5 2.5 0 1 1 12 6.5a2.5 2.5 0 0 1 0 5z"/></svg>
        <span>3-4817 Fernwick Avenue<br>Abbotsford, BC, V8K 2P9</span>
      </li>
    </ul>
  </section>

  <section class="card card--back">
    <div class="card__texture" role="img" aria-label="Fine grey wavy line pattern across the lower card"></div>
    <p class="back__logo">QL Resin Haus</p>
  </section>
</main>
</body>
</html>
```